Business Card Design Project

I am looking for a minimal matte background/shiny (spot UV) ink monochromatic design with a splash of neon color.

the card should be 2 sided, logo only on one side - all info and possibly logo on the other.

My creative director described the colors he imagined for the design to be:
'it's a dark field, like charcoal or a really dark burgundy, or deep blue, shot through with a neon—but just a tiny bit of it. so a charcoal field with a laser-thin streak of electric lime, safety orange, or cobalt blue. really beautiful stuff.'

here are some samples of the types of cards I am trying to create:
http://www.pictavault.example/photos/dawnpress/6967376935/in/photostream -> Vandrelle Lustre

http://www.pictavault.example/photos/dawnpress/6497659409/in/photostream -> Standard Coated (14pt/matte) with SPOT UV

http://www.pictavault.example/photos/dawnpress/6497658995/in/photostream/ -> Heavy Corvane with Raised Ink

http://www.pictavault.example/photos/dawnpress/6275629165/in/photostream/ -> Standard Coated (14pt/matte) with SPOT UV

Here is my logo:
https://www.filecrate.example/s/sigym192mlh58ge/quillorb%20logotype%20final.ai

Here are the details for info:
Dorian Elwood Marsh
email - dorian@quillorb.example
mobile - 555 013 2867
web -
quillorb.example: inventive technology applications
quillorb-tv.example: innovative video advertising

please let me know if there is anything at all that you need.

Target Market(s)

mid to large agencies that require interactive design and entrepreneurial/startup individuals/companies that need application development.

Industry/Entity Type

Safety

Requirements
Must have
• logo only on one side

```html
<!DOCTYPE html>
<html lang="en">
<head>
<meta charset="utf-8">
<title>Quillorb business card</title>
<link rel="stylesheet" href="https://fonts.googleapis.com/css2?family=Barlow:wght@400;500&display=swap">
<style>
  :root {
    --backdrop: #3a332f;
    --card: #2b2b2c;
    --card-edge: #232324;
    --gloss-ink: #141415;
    --white-ink: #f2f2f2;
    --soft-ink: #c9c9c9;
    --lime: #7ac21e;
  }
  * { box-sizing: border-box; margin: 0; padding: 0; }
  html, body {
    width: 1200px; height: 716px; overflow: hidden;
    background: var(--backdrop);
    font-family: "Barlow", Arial, sans-serif;
  }
  .canvas {
    position: relative; width: 1200px; height: 716px;
    display: flex; align-items: center; justify-content: center; gap: 40px;
  }
  .card {
    position: relative; width: 540px; height: 309px;
    background: var(--card);
    border: 1px solid var(--card-edge);
    box-shadow: 0 14px 30px rgba(0,0,0,0.45);
  }
  .wordmark {
    display: flex; align-items: center; gap: 14px;
    font-weight: 500; text-transform: uppercase; letter-spacing: 0.32em;
  }
  .wordmark-square { width: 16px; height: 16px; }
  .card-front .wordmark {
    position: absolute; left: 50%; top: 50%; transform: translate(-50%, -50%);
    font-size: 46px; color: var(--gloss-ink);
  }
  .card-front .wordmark-square { width: 24px; height: 24px; background: var(--gloss-ink); }
  .card-back .wordmark {
    position: absolute; right: 34px; top: 58px;
    font-size: 28px; color: var(--white-ink);
  }
  .card-back .wordmark-square { background: var(--white-ink); }
  .contact {
    position: absolute; left: 34px; top: 108px;
    color: var(--soft-ink); font-size: 14px; line-height: 1.35;
  }
  .contact-name { color: var(--lime); font-size: 19px; }
  .contact-role { margin-bottom: 12px; }
  .sites {
    position: absolute; left: 290px; top: 160px; list-style: none;
    color: var(--soft-ink);
  }
  .site { margin-bottom: 16px; }
  .site-address { font-size: 17px; color: var(--white-ink); }
  .site-tagline { display: flex; align-items: center; gap: 6px; font-size: 13px; }
  .site-tagline::before {
    content: ""; width: 2px; height: 10px; background: var(--lime);
  }
</style>
</head>
<body>
  <main class="canvas">
    <section class="card card-front" aria-label="Card front">
      <div class="wordmark">Quillorb<span class="wordmark-square"></span></div>
    </section>
    <section class="card card-back" aria-label="Card back">
      <div class="contact">
        <p class="contact-name">Dorian Elwood Marsh</p>
        <p class="contact-role">Founder &amp; CEO</p>
        <p class="contact-phone">555 013 2867</p>
        <p class="contact-email">dorian@quillorb.example</p>
      </div>
      <div class="wordmark">Quillorb<span class="wordmark-square"></span></div>
      <ul class="sites">
        <li class="site">
          <p class="site-address">quillorb.example</p>
          <p class="site-tagline">inventive technology applications</p>
        </li>
        <li class="site">
          <p class="site-address">quillorb-tv.example</p>
          <p class="site-tagline">innovative video advertising</p>
        </li>
      </ul>
    </section>
  </main>
</body>
</html>
```